BRAVEN POWERLINE SERVICES needs a vibrant design for electrical contracting work.

I require a card design for my own electrical contracting business. I will be doing a lot of domestic and commercial work, including things such as repairs, maintenance, lighting, installations and various others. LED lighting and energy efficiency will be a big part of my business. I wish not to have childish pictures such as light bulbs in the design, but rather a smart and modern looking card which incorporates my logo colours and perhaps the same lighting strike within the faded background of the card.

Target Market(s)

Residential and Commercial property owners.

Industry/Entity Type

Electrical

Contact Information for Business Card

Dalen Voskic
EC40923
Phone Number: 0417 358 942
Email: dalen@bravenpowerline.com

Font styles to use
Serif
Sans Serif

Requirements
Must have
• My Logo and associated colours.
Nice to have
• Some form of shapes splitting the card into different colours related to the colours of my logo. Electric Blue, Silver/Grey and White.
Should not have
• Childish pictures and symbols such as light bulbs.

```html
<!DOCTYPE html>
<html lang="en">
<head>
<meta charset="utf-8">
<title>Braven Powerline Services – Business Card</title>
<link rel="stylesheet" href="https://fonts.googleapis.com/css2?family=Lato:wght@400;700;900&family=Libre+Baskerville:wght@400;700&display=swap">
<style>
  :root {
    --backdrop: #2a2a2c;
    --electric-blue: #1f1ff0;
    --electric-blue-deep: #1010c8;
    --logo-blue: #1a2bd6;
    --white: #ffffff;
    --paper: #f2f2f2;
    --silver: #8a8a8a;
    --silver-dark: #5e5e5e;
    --divider: #3a3a3a;
    --panel-text: #f4f4f4;
  }
  * { box-sizing: border-box; margin: 0; padding: 0; }
  html, body { width: 1200px; height: 873px; overflow: hidden; }
  body {
    background: var(--backdrop);
    font-family: "Lato", Arial, sans-serif;
    position: relative;
  }
  .card {
    position: absolute;
    left: 300px;
    width: 600px;
    height: 343px;
    border-radius: 18px;
    overflow: hidden;
  }

  /* ---------- Back side ---------- */
  .card-back {
    top: 63px;
    background: linear-gradient(135deg, var(--electric-blue) 0%, var(--electric-blue-deep) 100%);
  }
  .card-back .faint-ring {
    position: absolute;
    left: 110px;
    top: 56px;
    width: 230px;
    height: 230px;
    border-radius: 50%;
    border: 26px solid rgba(255,255,255,0.28);
  }
  .card-back .brand {
    position: absolute;
    right: 34px;
    top: 150px;
    display: flex;
    align-items: center;
    gap: 10px;
  }
  .card-back .brand-dot {
    width: 26px; height: 26px; border-radius: 50%;
    border: 3px solid var(--white);
  }
  .card-back .brand-name {
    font-weight: 900;
    font-size: 16px;
    letter-spacing: 0.5px;
    color: var(--white);
    line-height: 1.1;
  }

  /* ---------- Front side ---------- */
  .card-front { top: 467px; background: var(--paper); }
  .card-front .shapes { position: absolute; inset: 0; }
  .card-front .brand {
    position: absolute;
    left: 30px;
    top: 150px;
    display: flex;
    align-items: center;
    gap: 10px;
  }
  .card-front .brand-dot {
    width: 40px; height: 40px; border-radius: 50%;
    border: 4px solid var(--silver);
    flex: none;
  }
  .card-front .brand-name {
    font-weight: 900;
    font-size: 19px;
    color: var(--logo-blue);
    line-height: 1.15;
    letter-spacing: 0.4px;
  }
  .details {
    position: absolute;
    left: 402px;
    top: 16px;
    width: 186px;
    color: var(--panel-text);
  }
  .name-tag, .section-tag {
    display: inline-block;
    background: var(--white);
    color: var(--logo-blue);
    font-family: "Libre Baskerville", Georgia, serif;
    font-weight: 700;
    text-transform: uppercase;
    padding: 2px 8px;
  }
  .name-tag { font-size: 15px; letter-spacing: 0.6px; }
  .contact-list { list-style: none; margin-top: 10px; }
  .contact-list li {
    display: flex;
    align-items: flex-start;
    gap: 7px;
    font-size: 10.5px;
    line-height: 1.35;
    margin-bottom: 3px;
  }
  .contact-list svg { flex: none; margin-top: 2px; }
  .section-tag { font-size: 13px; margin: 12px 0 0 36px; padding: 2px 14px; }
  .service-list {
    margin: 10px 0 0 28px;
    font-size: 13px;
    font-weight: 700;
    line-height: 1.55;
  }
  .service-list li::marker { font-size: 10px; }
</style>
</head>
<body>

<section class="card card-back" aria-label="Business card back">
  <div class="faint-ring" aria-hidden="true"></div>
  <div class="brand">
    <span class="brand-dot" aria-hidden="true"></span>
    <span class="brand-name">BRAVEN POWERLINE<br>SERVICES</span>
  </div>
</section>

<section class="card card-front" aria-label="Business card front">
  <svg class="shapes" width="600" height="343" viewBox="0 0 600 343" aria-hidden="true">
    <defs>
      <linearGradient id="panelShade" x1="0" y1="0" x2="1" y2="1">
        <stop offset="0" stop-color="#7d7d7d"/>
        <stop offset="1" stop-color="#565656"/>
      </linearGradient>
    </defs>
    <rect width="600" height="343" fill="var(--paper)"/>
    <polygon points="385,0 600,0 600,343 395,343" fill="url(#panelShade)"/>
    <polygon points="385,0 397,0 407,343 395,343" fill="var(--divider)"/>
  </svg>

  <div class="brand">
    <span class="brand-dot" aria-hidden="true"></span>
    <span class="brand-name">BRAVEN POWERLINE<br>SERVICES</span>
  </div>

  <div class="details">
    <span class="name-tag">Dalen Voskic</span>
    <ul class="contact-list">
      <li>
        <svg width="9" height="11" viewBox="0 0 9 11" aria-hidden="true"><rect x="1" y="0.5" width="7" height="10" rx="1.2" fill="none" stroke="#fff" stroke-width="1.2"/></svg>
        0417 358 942
      </li>
      <li>
        <svg width="11" height="8" viewBox="0 0 11 8" aria-hidden="true"><rect width="11" height="8" fill="#fff"/><path d="M0 0 L5.5 4.5 L11 0" fill="none" stroke="#666" stroke-width="1"/></svg>
        dalen@bravenpowerline.com
      </li>
      <li>
        <svg width="9" height="12" viewBox="0 0 9 12" aria-hidden="true"><path d="M4.5 0 A4.5 4.5 0 0 1 9 4.5 C9 7.5 4.5 12 4.5 12 C4.5 12 0 7.5 0 4.5 A4.5 4.5 0 0 1 4.5 0 Z" fill="#fff"/><circle cx="4.5" cy="4.5" r="1.6" fill="#666"/></svg>
        <span>2480 N. Harbor Lane<br>Westfield, Fl 33190</span>
      </li>
    </ul>
    <span class="section-tag">My Services</span>
    <ul class="service-list">
      <li>Repairs</li>
      <li>Maintenance</li>
      <li>Installations</li>
      <li>LED lighting</li>
      <li>Energy Efficiency</li>
    </ul>
  </div>
</section>

</body>
</html>
```